Las Vegas Themed Video & Messaging Zelpad App

We have designed an Zelpad app that allows people to share videos and message one another while visiting Las Vegas, Nevada. However, without a simple, compelling design this app will be "just like the rest". This is where you come in.

As a version 1.0 of this app, we want to test the market as inexpensively as possible. There are other screens that we will need to be designed; during development we will be coming back to you for further iterations and enhancements. Consider this contest a paid interview, in other words.

This app will be available to users in the Quorvo Apps Mart. A mockup is attached to the Files section of this brief.

Our mockup is intentionally devoid of almost all styling because we did not want to get in front of your design. The attached mockup exists only to give you a general guide towards the "feel" of the app, but the elements themselves and their placements can (and should) be freely changed by you.

Please be creative; we're excited to see your work!

Requirements
Must have
• Simplicity is the focus. We'd like to see only a few screens from you to judge your work:

• The home screen.
• The messaging screen.
• A screen that records a video.

Nice to have
• A clean, contemporary design:

• Beautiful typography.
• A "flat-ish" design, avoiding skeuomorphism.

```html
<!DOCTYPE html>
<html lang="en">
<head>
<meta charset="utf-8">
<title>NEONREEL – app screens</title>
<link rel="stylesheet" href="https://fonts.googleapis.com/css2?family=Source+Sans+3:wght@400;600;700&family=Arimo:wght@400;700&display=swap">
<style>
  :root{
    --blue:#0b6fc0;
    --blue-dark:#075aa0;
    --blue-light:#2f8bd6;
    --ink:#111;
    --card-top:#ffffff;
    --card-bottom:#d4ebf8;
    --thumb-top:#6b6b6b;
    --thumb-bottom:#141414;
    --key:#f7f7f7;
    --key-dark:#c9ccd2;
    --kb-bg:#d7dbe1;
    --rec:#e0242a;
    --white:#fff;
  }
  *{box-sizing:border-box;margin:0;padding:0}
  html,body{width:1200px;height:800px;overflow:hidden;background:var(--white)}
  body{position:relative;font-family:"Source Sans 3",Arial,sans-serif;color:var(--ink)}
  .icons{position:absolute;width:0;height:0}
  .screen{position:absolute;top:171px;width:260px;height:461px;overflow:hidden;background:var(--blue)}
  .screen--splash{left:22px}
  .screen--home{left:330px}
  .screen--chat{left:628px}
  .screen--mine{left:922px}

  .status-bar{position:absolute;top:0;left:0;right:0;height:15px;background:#000;color:var(--white);
    font:700 10px/15px Arimo,Arial,sans-serif;display:flex;align-items:center;padding:0 4px}
  .status-bar .carrier{display:flex;align-items:center;gap:3px}
  .status-bar .time{position:absolute;left:0;right:0;text-align:center}
  .status-bar .battery{margin-left:auto}
  .status-bar svg{display:block}

  .top-bar{position:absolute;top:15px;left:0;right:0;height:38px;
    background:linear-gradient(var(--blue-light),var(--blue-dark));display:flex;align-items:center;padding:0 6px}
  .chips{height:27px;width:46px;border:1px solid #5fa3dc;border-radius:3px;background:var(--blue-dark);
    color:var(--white);font-weight:700;font-size:15px;display:flex;align-items:center;justify-content:center;letter-spacing:-.5px}
  .chips small{font-size:10px;font-weight:600}
  .brand{flex:1;display:flex;align-items:center;justify-content:center;gap:4px;color:var(--white);
    font-weight:700;font-size:19px;letter-spacing:.5px}
  .brand .dot{width:13px;height:13px;border-radius:50%;background:var(--white)}
  .square-btn{width:26px;height:26px;border:1px solid #5fa3dc;border-radius:3px;background:var(--blue-dark);
    display:flex;align-items:center;justify-content:center}
  .top-bar .title{flex:1;text-align:center;color:var(--white);font-weight:700;font-size:18px}

  .splash-brand{position:absolute;top:215px;left:0;right:0;display:flex;justify-content:center;align-items:center;gap:5px;
    color:var(--white);font-weight:700;font-size:28px;letter-spacing:1px}
  .splash-brand .dot{width:20px;height:20px;border-radius:50%;background:var(--white)}

  .search-band{position:absolute;top:53px;left:0;right:0;height:46px;background:var(--blue)}
  .search{position:absolute;left:8px;right:8px;top:14px;height:20px;border-radius:10px;background:var(--white);
    display:flex;align-items:center;gap:4px;padding-left:6px;color:#9a9a9a;font-size:14px}
  .section-title{position:absolute;top:53px;left:0;right:0;height:46px;background:var(--blue);color:var(--white);
    font-weight:700;font-size:18px;text-align:center;line-height:46px}

  .video-list{position:absolute;top:99px;left:0;right:0;list-style:none}
  .video-item{height:106px;background:linear-gradient(var(--card-top),var(--card-bottom));position:relative;border-bottom:1px solid #c3dcec}
  .thumb{position:absolute;left:8px;top:13px;width:94px;height:80px;
    background:linear-gradient(var(--thumb-top) 0%,#2b2b2b 50%,var(--thumb-bottom) 50%,#1c1c1c 100%)}
  .thumb .play{position:absolute;right:4px;bottom:5px}
  .meta{position:absolute;left:113px;top:12px}
  .author{display:flex;align-items:center;gap:4px;font-weight:700;font-size:14px}
  .meta .mail{display:block;margin-top:4px}
  .video-title{font-size:14px;margin-top:3px}
  .duration{font-size:9px;margin-left:2px;line-height:1}
  .screen--mine .video-title{margin-top:1px}

  .tab-bar{position:absolute;bottom:0;left:0;right:0;height:45px;background:var(--blue);display:flex}
  .tab{flex:1;display:flex;flex-direction:column;align-items:center;justify-content:flex-end;padding-bottom:3px;
    color:var(--white);font-size:9px;gap:2px;border-left:1px solid #6aa8dc}
  .tab:first-child{border-left:0}

  .thread{position:absolute;top:53px;left:0;right:0}
  .message{height:86px;margin-top:6px;background:linear-gradient(var(--card-top),var(--card-bottom));position:relative}
  .message + .message{margin-top:4px;height:90px}
  .message .author{position:absolute;left:12px;top:8px}
  .message .date{position:absolute;left:42px;top:26px;font-size:8px;font-weight:600}
  .message .body{position:absolute;left:10px;right:10px;top:37px;height:36px;background:var(--white);
    border:1px solid #b9b9b9;font-size:8px;padding:1px 3px}

  .composer{position:absolute;top:245px;left:0;right:0;height:42px;background:var(--blue);display:flex;align-items:center;padding:0 6px;gap:6px}
  .composer .field{flex:1;height:20px;border-radius:10px;background:var(--white);font-size:13px;padding-left:14px;line-height:20px}
  .composer .send{height:24px;padding:0 6px;border:1px solid #5fa3dc;border-radius:3px;background:var(--blue-dark);color:var(--white);
    font-weight:600;font-size:15px;line-height:22px}

  .keyboard{position:absolute;top:287px;left:0;right:0;bottom:0;background:var(--kb-bg);padding:8px 2px 0;
    font-family:Arimo,Arial,sans-serif}
  .kb-row{display:flex;justify-content:center;gap:4px;margin-bottom:10px}
  .key{width:22px;height:30px;border-radius:4px;background:var(--key);box-shadow:0 1px 1px #8c8f94;
    font-size:17px;display:flex;align-items:center;justify-content:center}
  .key--dark{background:var(--key-dark)}
  .key--wide{width:30px}
  .key--blue{background:var(--blue);color:var(--white);font-size:13px}
  .kb-row--bottom{gap:4px}
  .kb-row--bottom .key{height:30px;font-size:13px}

  .record-bar{position:absolute;bottom:0;left:0;right:0;height:45px;background:var(--blue);display:flex;align-items:center;color:var(--white)}
  .rec-dot{width:32px;height:32px;border:3px solid var(--rec);border-radius:50%;margin-left:13px}
  .record-bar .label{margin-left:10px;font-size:19px;flex:1}
  .settings{width:55px;height:45px;border-left:1px solid #6aa8dc;display:flex;flex-direction:column;align-items:center;justify-content:flex-end;padding-bottom:3px;font-size:9px;gap:1px}
</style>
</head>
<body>

<svg class="icons" aria-hidden="true">
  <symbol id="i-person" viewBox="0 0 24 24"><circle cx="12" cy="7" r="6" fill="currentColor"/><path d="M1 24c0-7 5-10 11-10s11 3 11 10z" fill="currentColor"/></symbol>
  <symbol id="i-mail" viewBox="0 0 24 18"><rect x="1" y="1" width="22" height="16" fill="currentColor"/><path d="M1 1l11 9 11-9M1 17l8-7M23 17l-8-7" fill="none" stroke="#fff" stroke-width="1.5"/></symbol>
  <symbol id="i-play" viewBox="0 0 20 20"><circle cx="10" cy="10" r="10" fill="#111"/><circle cx="10" cy="10" r="9" fill="#eee"/><circle cx="10" cy="10" r="7.5" fill="#1a1a1a"/><path d="M8 6l6 4-6 4z" fill="#fff"/></symbol>
  <symbol id="i-plus" viewBox="0 0 20 20"><path d="M10 2v16M2 10h16" stroke="#fff" stroke-width="3"/></symbol>
</svg>

<!-- Splash -->
<section class="screen screen--splash" aria-label="Splash screen">
  <div class="status-bar">
    <span class="carrier"><svg width="14" height="8"><rect x="0" y="6" width="2" height="2" fill="#fff"/><rect x="3" y="4" width="2" height="4" fill="#fff"/><rect x="6" y="2" width="2" height="6" fill="#fff"/><rect x="9" y="0" width="2" height="8" fill="#fff"/></svg>Nexa
      <svg width="13" height="9" viewBox="0 0 13 9"><path d="M1 3.5a8 8 0 0 1 11 0M3 5.5a5 5 0 0 1 7 0M5 7.5a2 2 0 0 1 3 0" stroke="#fff" stroke-width="1.5" fill="none"/></svg></span>
    <span class="time">12:34 PM</span>
    <svg class="battery" width="18" height="9"><rect x=".5" y=".5" width="15" height="8" fill="none" stroke="#fff"/><rect x="2" y="2" width="12" height="5" fill="#fff"/><rect x="16" y="3" width="2" height="3" fill="#fff"/></svg>
  </div>
  <div class="splash-brand">NEONREEL<span class="dot"></span></div>
</section>

<!-- Home -->
<section class="screen screen--home" aria-label="Home screen">
  <div class="status-bar">
    <span class="carrier"><svg width="14" height="8"><rect x="0" y="6" width="2" height="2" fill="#fff"/><rect x="3" y="4" width="2" height="4" fill="#fff"/><rect x="6" y="2" width="2" height="6" fill="#fff"/><rect x="9" y="0" width="2" height="8" fill="#fff"/></svg>Nexa
      <svg width="13" height="9" viewBox="0 0 13 9"><path d="M1 3.5a8 8 0 0 1 11 0M3 5.5a5 5 0 0 1 7 0M5 7.5a2 2 0 0 1 3 0" stroke="#fff" stroke-width="1.5" fill="none"/></svg></span>
    <span class="time">12:34 PM</span>
    <svg class="battery" width="18" height="9"><rect x=".5" y=".5" width="15" height="8" fill="none" stroke="#fff"/><rect x="2" y="2" width="12" height="5" fill="#fff"/><rect x="16" y="3" width="2" height="3" fill="#fff"/></svg>
  </div>
  <header class="top-bar">
    <div class="chips">20<small>Chips</small></div>
    <div class="brand">NEONREEL<span class="dot"></span></div>
    <div class="square-btn"><svg width="16" height="16"><use href="#i-plus"/></svg></div>
  </header>
  <div class="search-band">
    <div class="search"><svg width="12" height="12" viewBox="0 0 12 12"><circle cx="5" cy="5" r="3.5" stroke="#111" stroke-width="2" fill="none"/><path d="M7.5 7.5l3.5 3.5" stroke="#111" stroke-width="2"/></svg>Search By Username Or Hashtag</div>
  </div>
  <ul class="video-list">
    <li class="video-item">
      <div class="thumb" role="img" aria-label="Video thumbnail"><svg class="play" width="20" height="20"><use href="#i-play"/></svg></div>
      <div class="meta">
        <div class="author"><svg width="24" height="24" color="#0b6fc0"><use href="#i-person"/></svg>Ved aru</div>
        <svg class="mail" width="24" height="18" color="#0b6fc0"><use href="#i-mail"/></svg>
        <div class="video-title">VideoTitle</div><div class="duration">01:05</div>
      </div>
    </li>
    <li class="video-item">
      <div class="thumb" role="img" aria-label="Video thumbnail"><svg class="play" width="20" height="20"><use href="#i-play"/></svg></div>
      <div class="meta">
        <div class="author"><svg width="24" height="24" color="#0b6fc0"><use href="#i-person"/></svg>Ved aru</div>
        <svg class="mail" width="24" height="18" color="#0b6fc0"><use href="#i-mail"/></svg>
        <div class="video-title">VideoTitle</div><div class="duration">01:05</div>
      </div>
    </li>
    <li class="video-item">
      <div class="thumb" role="img" aria-label="Video thumbnail"><svg class="play" width="20" height="20"><use href="#i-play"/></svg></div>
      <div class="meta">
        <div class="author"><svg width="24" height="24" color="#0b6fc0"><use href="#i-person"/></svg>Ved aru</div>
        <svg class="mail" width="24" height="18" color="#0b6fc0"><use href="#i-mail"/></svg>
        <div class="video-title">VideoTitle</div><div class="duration">01:05</div>
      </div>
    </li>
  </ul>
  <nav class="tab-bar">
    <div class="tab"><svg width="26" height="26" viewBox="0 0 26 26"><circle cx="13" cy="13" r="11" stroke="#fff" stroke-width="2.5" fill="none"/><path d="M13 6v7h6" stroke="#fff" stroke-width="2.5" fill="none"/></svg>Newest</div>
    <div class="tab"><svg width="28" height="26" viewBox="0 0 28 26"><path d="M14 1l3.8 8 8.7 1-6.4 6 1.7 8.6L14 20.3 6.2 24.6 7.9 16 1.5 10l8.7-1z" stroke="#fff" stroke-width="2" fill="none"/></svg>Most View</div>
    <div class="tab"><svg width="26" height="26" viewBox="0 0 26 26"><circle cx="13" cy="8" r="6" stroke="#fff" stroke-width="2" fill="none"/><path d="M2 25c0-7 5-10 11-10s11 3 11 10z" stroke="#fff" stroke-width="2" fill="none"/></svg>Your Videos</div>
    <div class="tab"><svg width="28" height="10" viewBox="0 0 28 10"><circle cx="4" cy="5" r="4" fill="#fff"/><circle cx="14" cy="5" r="4" fill="#fff"/><circle cx="24" cy="5" r="4" fill="#fff"/></svg><span style="margin-top:6px">More</span></div>
  </nav>
</section>

<!-- Messaging -->
<section class="screen screen--chat" aria-label="Messaging screen">
  <div class="status-bar">
    <span class="carrier"><svg width="14" height="8"><rect x="0" y="6" width="2" height="2" fill="#fff"/><rect x="3" y="4" width="2" height="4" fill="#fff"/><rect x="6" y="2" width="2" height="6" fill="#fff"/><rect x="9" y="0" width="2" height="8" fill="#fff"/></svg>Nexa
      <svg width="13" height="9" viewBox="0 0 13 9"><path d="M1 3.5a8 8 0 0 1 11 0M3 5.5a5 5 0 0 1 7 0M5 7.5a2 2 0 0 1 3 0" stroke="#fff" stroke-width="1.5" fill="none"/></svg></span>
    <span class="time">12:34 PM</span>
    <svg class="battery" width="18" height="9"><rect x=".5" y=".5" width="15" height="8" fill="none" stroke="#fff"/><rect x="2" y="2" width="12" height="5" fill="#fff"/><rect x="16" y="3" width="2" height="3" fill="#fff"/></svg>
  </div>
  <header class="top-bar">
    <div class="chips">20<small>Chips</small></div>
    <div class="title">User Handle</div>
    <div class="square-btn" style="background:#fff"><svg width="20" height="20" color="#0b6fc0"><use href="#i-person"/></svg></div>
  </header>
  <div class="thread">
    <article class="message">
      <div class="author"><svg width="24" height="24" color="#0b6fc0"><use href="#i-person"/></svg>Ved aru</div>
      <div class="date">31-05-2013</div>
      <p class="body">Sample message text.</p>
    </article>
    <article class="message">
      <div class="author"><svg width="24" height="24" color="#0b6fc0"><use href="#i-person"/></svg>Ved aru</div>
      <div class="date">01-06-2013</div>
      <p class="body">Sample message text.</p>
    </article>
  </div>
  <div class="composer">
    <div class="square-btn" style="width:26px;height:24px"><svg width="14" height="14"><use href="#i-plus"/></svg></div>
    <div class="field">Sample message text.</div>
    <div class="send">Send</div>
  </div>
  <div class="keyboard" aria-label="Keyboard">
    <div class="kb-row"><span class="key">Q</span><span class="key">W</span><span class="key">E</span><span class="key">R</span><span class="key">T</span><span class="key">Y</span><span class="key">U</span><span class="key">I</span><span class="key">O</span><span class="key">P</span></div>
    <div class="kb-row"><span class="key">A</span><span class="key">S</span><span class="key">D</span><span class="key">F</span><span class="key">G</span><span class="key">H</span><span class="key">J</span><span class="key">K</span><span class="key">L</span></div>
    <div class="kb-row"><span class="key key--blue key--wide"><svg width="16" height="16" viewBox="0 0 16 16"><path d="M8 1L1 8h4v6h6V8h4z" stroke="#fff" stroke-width="1.5" fill="none"/></svg></span><span class="key">Z</span><span class="key">X</span><span class="key">C</span><span class="key">V</span><span class="key">B</span><span class="key">N</span><span class="key">M</span><span class="key key--blue key--wide"><svg width="18" height="12" viewBox="0 0 18 12"><path d="M5 0h13v12H5L0 6z" fill="#fff"/><path d="M9 3l6 6M15 3l-6 6" stroke="#0b6fc0" stroke-width="1.8"/></svg></span></div>
    <div class="kb-row kb-row--bottom"><span class="key key--blue" style="width:56px">.?123</span><span class="key key--dark" style="width:36px;font-size:11px;color:#555">space</span><span class="key" style="width:36px">@</span><span class="key key--dark" style="width:36px">.</span><span class="key key--blue" style="width:60px">return</span></div>
  </div>
</section>

<!-- My Videos / record -->
<section class="screen screen--mine" aria-label="My videos and recording screen">
  <div class="status-bar">
    <span class="carrier"><svg width="14" height="8"><rect x="0" y="6" width="2" height="2" fill="#fff"/><rect x="3" y="4" width="2" height="4" fill="#fff"/><rect x="6" y="2" width="2" height="6" fill="#fff"/><rect x="9" y="0" width="2" height="8" fill="#fff"/></svg>Nexa
      <svg width="13" height="9" viewBox="0 0 13 9"><path d="M1 3.5a8 8 0 0 1 11 0M3 5.5a5 5 0 0 1 7 0M5 7.5a2 2 0 0 1 3 0" stroke="#fff" stroke-width="1.5" fill="none"/></svg></span>
    <span class="time">12:34 PM</span>
    <svg class="battery" width="18" height="9"><rect x=".5" y=".5" width="15" height="8" fill="none" stroke="#fff"/><rect x="2" y="2" width="12" height="5" fill="#fff"/><rect x="16" y="3" width="2" height="3" fill="#fff"/></svg>
  </div>
  <header class="top-bar">
    <div class="chips">20<small>Chips</small></div>
    <div class="brand">NEONREEL<span class="dot"></span></div>
    <div class="square-btn"><svg width="16" height="16"><use href="#i-plus"/></svg></div>
  </header>
  <h2 class="section-title">My Videos</h2>
  <ul class="video-list">
    <li class="video-item">
      <div class="thumb" role="img" aria-label="Video thumbnail"><svg class="play" width="20" height="20"><use href="#i-play"/></svg></div>
      <div class="meta">
        <div class="author"><svg width="24" height="24" color="#0b6fc0"><use href="#i-person"/></svg>Ved aru</div>
        <div class="video-title">VideoTitle</div><div class="duration">01:05</div>
      </div>
    </li>
    <li class="video-item">
      <div class="thumb" role="img" aria-label="Video thumbnail"><svg class="play" width="20" height="20"><use href="#i-play"/></svg></div>
      <div class="meta">
        <div class="author"><svg width="24" height="24" color="#0b6fc0"><use href="#i-person"/></svg>Ved aru</div>
        <div class="video-title">VideoTitle</div><div class="duration">01:05</div>
      </div>
    </li>
    <li class="video-item">
      <div class="thumb" role="img" aria-label="Video thumbnail"><svg class="play" width="20" height="20"><use href="#i-play"/></svg></div>
      <div class="meta">
        <div class="author"><svg width="24" height="24" color="#0b6fc0"><use href="#i-person"/></svg>Ved aru</div>
        <div class="video-title">VideoTitle</div><div class="duration">01:05</div>
      </div>
    </li>
  </ul>
  <div class="record-bar">
    <span class="rec-dot"></span>
    <span class="label">Rec/Share Video</span>
    <div class="settings"><svg width="26" height="26" viewBox="0 0 26 26"><g fill="#fff"><circle cx="13" cy="13" r="8"/><rect x="11" y="0" width="4" height="6"/><rect x="11" y="20" width="4" height="6"/><rect x="0" y="11" width="6" height="4"/><rect x="20" y="11" width="6" height="4"/><rect x="11" y="0" width="4" height="6" transform="rotate(45 13 13)"/><rect x="11" y="20" width="4" height="6" transform="rotate(45 13 13)"/><rect x="0" y="11" width="6" height="4" transform="rotate(45 13 13)"/><rect x="20" y="11" width="6" height="4" transform="rotate(45 13 13)"/></g><circle cx="13" cy="13" r="3.5" fill="#0b6fc0"/></svg>Sethings</div>
  </div>
</section>

</body>
</html>
```